Wolkenfeld - a property developer - Website design

Hi all!
Exciting new project for you! :)
We are looking for some creative/modern designs to best represent us as a company.
Please have a look at the following link: huhu.wolkenfeld.eu to get an idea about who we are and what we do.
The 'Main Page' of the HP should be neatly arranged, easy to navigate, contain several pictures (changing every 10 seconds or so) that should reflect that we are property developers.
The navigation points ('About us', 'Projects' 'Investment', 'Contact Us', 'Legal Notice') should be included in the Design (again under every navigation point, pictures may be added - that reflect our profession and/or the subsection)
What we will need at the end of the day is a fully functional site - i.e: a site that is designed and programmed with backend/wordpress, to allow us to make changes anytime we feel like it.
Further questions?! Don't hesitate to contact me! Thanks :)
Target Market(s)
Real Estate Development/Building sector
Industry/Entity Type
Real Estate Development
Number of Pages Required
5+ page
Look and feel

```html
<!DOCTYPE html>
<html lang="en">
<head>
<meta charset="utf-8">
<title>Wolkenfeld – Property Developer</title>
<link href="https://fonts.googleapis.com/css2?family=Exo+2:wght@500;600;700&family=Lato:wght@400;700&family=Roboto:ital,wght@0,400;0,500;1,400&display=swap" rel="stylesheet">
<style>
:root{
  --maroon:#4a1029;
  --maroon-light:#6b2443;
  --green:#8cc63f;
  --grey-bg:#e9e9e9;
  --text:#555;
  --footer:#333;
  --footer-bottom:#1b1b1b;
  --white:#fff;
}
*{margin:0;padding:0;box-sizing:border-box}
html,body{width:1200px;height:2214px;overflow:hidden}
body{position:relative;background:var(--white);font-family:"Lato",sans-serif;color:var(--text)}
.abs{position:absolute}

/* header */
.topbar{left:0;top:0;width:1200px;height:77px;background:#ececec}
.brand{left:100px;top:14px;display:flex;align-items:center;gap:10px}
.brand-square{width:26px;height:48px;background:#222}
.brand-name{font-family:"Exo 2",sans-serif;font-weight:600;font-size:34px;color:var(--maroon);letter-spacing:1px;line-height:1}
.brand-sub{font-family:"Exo 2",sans-serif;font-size:10px;color:var(--maroon);margin-top:3px}
.social-top{left:873px;top:26px;display:flex;gap:5px}
.social-top span{width:28px;height:28px;background:#888}
.lang{left:1013px;top:25px;width:88px;height:28px;background:#fff;border:1px solid #ddd;font-size:12px;display:flex;align-items:center;gap:6px;padding-left:8px;color:#333}
.lang i{width:18px;height:12px;background:#28407a;display:block}
.lang b{border:4px solid transparent;border-top-color:#555;margin-top:4px;margin-left:2px}

.nav{left:0;top:77px;width:1200px;height:44px;background:var(--maroon);border-bottom:2px solid #8a4a63}
.nav a{position:absolute;top:0;height:42px;line-height:42px;color:#fff;text-decoration:none;font-family:"Roboto",sans-serif;font-weight:500;font-size:15px}
.nav a.active{background:var(--maroon-light);padding:0 28px}
.call{right:99px;top:77px;height:44px;display:flex;align-items:center;gap:10px;color:#fff}
.call small{font-size:9px;font-family:"Roboto",sans-serif}
.call strong{font-family:"Roboto",sans-serif;font-style:italic;font-weight:400;font-size:22px}

/* hero */
.hero{left:0;top:121px;width:1200px;height:425px;background:linear-gradient(180deg,#8fb8df 0%,#cfdcea 45%,#e5e8e4 70%,#6f9a54 92%,#e8ece8 100%)}
.hero-caption{left:111px;top:387px;width:509px;height:100px;background:rgba(30,30,30,.72);padding:8px 14px;font-family:"Exo 2",sans-serif;font-weight:600;font-size:33px;line-height:42px;color:#fff}
.arrow{top:306px;width:33px;height:33px;background:rgba(40,40,40,.8);border:1px solid #999}
.arrow svg{display:block;margin:9px auto}

/* welcome */
.welcome-title{left:100px;top:586px;font-family:"Exo 2",sans-serif;font-weight:600;font-size:30px;color:#555}
.welcome-title em{font-style:normal;color:var(--maroon);font-weight:700}
.welcome-art{left:103px;top:638px;width:86px;height:174px;background:linear-gradient(180deg,#9a9a9a,#858585)}
.welcome-text{left:208px;top:639px;width:458px;font-size:11.5px;line-height:17.6px;color:#444}
.welcome-text p{margin-bottom:7px}
.more{font-weight:700;font-size:12px;color:#333}
.welcome-photo{left:738px;top:596px;width:363px;height:220px;background:linear-gradient(180deg,#4f7db3 0%,#a9c2da 55%,#d9dcd8 70%,#5f8c3c 100%);box-shadow:0 6px 10px rgba(0,0,0,.2)}

/* services */
.services{left:0;top:863px;width:1200px;height:231px;background:var(--green)}
.service{position:absolute;top:38px;width:240px;text-align:center;color:#fff}
.service svg{display:block;margin:0 auto 10px}
.service h3{font-family:"Roboto",sans-serif;font-weight:500;font-size:17px;margin-bottom:8px}
.service p{font-size:11.5px;line-height:17.5px;color:#f3f8ea;padding:0 16px}

/* projects */
.projects{left:0;top:1094px;width:1200px;height:552px;background:var(--grey-bg)}
.section-title{position:absolute;left:0;width:1200px;text-align:center;font-family:"Exo 2",sans-serif;font-weight:600;font-size:30px;color:#555}
.section-title em{font-style:normal;color:var(--maroon)}
.divider{position:absolute;left:492px;width:216px;height:1px;background:#bbb}
.divider::after{content:"";position:absolute;left:104px;top:-4px;width:8px;height:8px;border:1px solid #bbb;background:inherit;transform:rotate(45deg)}
.projects-lead{position:absolute;left:0;top:116px;width:1200px;text-align:center;font-size:13px;color:#666}
.grid{left:99px;top:1256px;width:1002px;height:346px;display:grid;grid-template-columns:repeat(4,1fr);grid-template-rows:repeat(2,1fr)}
.tile{position:relative}
.t1{background:linear-gradient(180deg,#5c6e86,#8e99a7)}
.t2{background:linear-gradient(180deg,#6e9ad0,#a9b9c8 60%,#5c8a3e)}
.t3{background:linear-gradient(180deg,#a9b8c8,#4a4c4e 60%,#a8a8a6)}
.t4{background:linear-gradient(180deg,#4f8fd6,#9cc3e6 55%,#3f7f3a)}
.t5{background:linear-gradient(180deg,#b8c6d0,#5c7a42 50%,#7f7a72)}
.t6{background:linear-gradient(180deg,#c4d4e4,#c9c3b8 60%,#6f8f4a)}
.t7{background:linear-gradient(180deg,#e4e8ec,#b6a58d 55%,#7a8a56)}
.t8{background:linear-gradient(180deg,#f2f2f2,#4a6a98 45%,#8c8174)}
.tile-overlay{position:absolute;left:17px;top:22px;width:217px;height:129px;border:1px solid #eee;background:rgba(60,60,60,.35);color:#fff;text-align:center;font-size:12px;line-height:17px;padding-top:40px}
.tile-overlay b{display:block;font-weight:700;margin-bottom:14px}

/* partners */
.partners-title{top:1686px}
.partner{position:absolute;top:1764px;width:230px;height:102px;border:1px solid #ddd;background:#f7f7f7;display:flex;align-items:center;justify-content:center;gap:10px;font-family:"Exo 2",sans-serif;font-weight:600;font-size:22px;color:#333}
.partner i{width:30px;height:30px;display:block}

/* footer */
.footer{left:0;top:1908px;width:1200px;height:262px;background:var(--footer);color:#ddd}
.fcol{position:absolute;top:59px}
.fcol h4{font-family:"Roboto",sans-serif;font-weight:500;font-size:17px;color:#fff;padding-bottom:8px;border-bottom:1px solid #555;margin-bottom:14px}
.links li{list-style:none;font-size:11.5px;font-weight:700;margin-bottom:8px;color:#fff}
.links li::before{content:"›";margin-right:8px;color:#aaa}
.contact li{list-style:none;display:flex;gap:14px;font-size:11.5px;line-height:17px;margin-bottom:11px;color:#eee}
.contact svg{flex:none;margin-top:2px}
.news p{font-size:11.5px;line-height:17px;margin-bottom:10px;color:#eee;width:200px}
.news .field{width:206px;height:30px;background:#fff;font-size:10px;font-style:italic;color:#999;padding:9px 8px}
.news .btn{display:inline-block;margin-top:12px;background:#5aa02c;color:#fff;font-size:12px;font-weight:700;padding:7px 12px}
.fbrand{left:906px;top:1998px;display:flex;align-items:center;gap:8px}
.fbrand i{width:18px;height:36px;background:#fff;display:block}
.fbrand span{font-family:"Exo 2",sans-serif;font-weight:600;font-size:28px;color:#fff}
.fsocial{left:938px;top:2077px;display:flex;gap:6px}
.fsocial span{width:27px;height:27px}
.copyright{left:0;top:2170px;width:1200px;height:44px;background:var(--footer-bottom);color:#ddd;font-size:11.5px;padding:16px 0 0 101px}
</style>
</head>
<body>

<header>
  <div class="abs topbar"></div>
  <div class="abs brand">
    <div class="brand-square"></div>
    <div>
      <div class="brand-name">WOLKENFELD</div>
      <div class="brand-sub">Wolkenfeld.at</div>
    </div>
  </div>
  <div class="abs social-top"><span></span><span></span><span></span><span></span></div>
  <div class="abs lang"><i></i>English<b></b></div>

  <nav class="abs nav">
    <a class="active" href="#" style="left:100px">Home</a>
    <a href="#" style="left:226px">About us</a>
    <a href="#" style="left:350px">Projects</a>
    <a href="#" style="left:468px">Investment</a>
    <a href="#" style="left:605px">Legal Notice</a>
    <a href="#" style="left:751px">Contact Us</a>
  </nav>
  <div class="abs call"><small>call us today</small><strong>+43 1000 2040</strong></div>
</header>

<section>
  <div class="abs hero" role="img" aria-label="Photo of tall white residential towers under a blue sky with trees in front"></div>
  <div class="abs arrow" style="left:15px"><svg width="12" height="14"><path d="M10 1 L2 7 L10 13 Z" fill="none" stroke="#fff" stroke-width="1.5"/></svg></div>
  <div class="abs arrow" style="left:1135px"><svg width="12" height="14"><path d="M2 1 L10 7 L2 13 Z" fill="none" stroke="#fff" stroke-width="1.5"/></svg></div>
  <h1 class="abs hero-caption">Helping You Find The<br>Property Of Your Dreams</h1>
</section>

<section>
  <h2 class="abs welcome-title">Welcome to <em>Wolkenfeld</em></h2>
  <div class="abs welcome-art" role="img" aria-label="Grey illustration of an apartment building"></div>
  <div class="abs welcome-text">
    <p>Lorem ipsum dolor sit amet, consectetur adipiscing elit. Curabitur lobortis, tellus in aliquam cursus, ante lorem tristique elit, at aliquet nunc ante et orci.</p>
    <p>It is a long established fact that a reader will be distracted by the readable content of a page when looking at its layout. The point of using Lorem Ipsum is that it has a more-or-less normal distribution of letters, as opposed to using 'Content here, content here', making it look like readable English. Many desktop publishing packages and web page editors now use Lorem Ipsum as their default model text, and a search for 'lorem ipsum' will uncover many web sites still in their infancy. Various versions</p>
    <p class="more">More More »</p>
  </div>
  <div class="abs welcome-photo" role="img" aria-label="Photo of a modern white multi-storey house on a lawn"></div>
</section>

<section class="abs services">
  <div class="service" style="left:84px">
    <svg width="56" height="56" viewBox="0 0 56 56" fill="none" stroke="#fff" stroke-width="2.5"><rect x="6" y="18" width="18" height="18"/><path d="M4 20 L15 10 L26 20"/><rect x="30" y="32" width="20" height="18"/><circle cx="40" cy="18" r="8"/></svg>
    <h3>New Projects</h3>
    <p>Lorem Ipsum is simply dummy text of the printing and typesetting industry.</p>
  </div>
  <div class="service" style="left:348px">
    <svg width="56" height="56" viewBox="0 0 56 56" fill="#fff"><rect x="4" y="4" width="3" height="48"/><rect x="4" y="49" width="48" height="3"/><rect x="14" y="34" width="6" height="15"/><rect x="24" y="28" width="6" height="21"/><rect x="34" y="22" width="6" height="27"/><rect x="44" y="14" width="6" height="35"/><path d="M12 30 L26 18 L34 22 L48 6" stroke="#fff" stroke-width="2.5" fill="none"/></svg>
    <h3>case study</h3>
    <p>There are many variations of passages of Lorem Ipsum available, but the majority</p>
  </div>
  <div class="service" style="left:611px">
    <svg width="56" height="56" viewBox="0 0 56 56" fill="none" stroke="#fff" stroke-width="3"><rect x="6" y="20" width="44" height="30"/><path d="M20 20 V12 H36 V20"/><path d="M6 32 H50"/></svg>
    <h3>Projects Development</h3>
    <p>Contrary to popular belief, Lorem Ipsum is not simply random text. It has roots in a piece</p>
  </div>
  <div class="service" style="left:873px">
    <svg width="56" height="56" viewBox="0 0 56 56" fill="none" stroke="#fff" stroke-width="3"><path d="M4 28 L28 6 L52 28"/><path d="M12 24 V50 H44 V24"/><circle cx="28" cy="34" r="7"/></svg>
    <h3>Effective Price</h3>
    <p>Lorem Ipsum is that it has a more-or-less normal distribution of letters, as opposed to</p>
  </div>
</section>

<section class="abs projects">
  <h2 class="section-title" style="top:33px">Our <em>Projects</em></h2>
  <div class="divider" style="top:82px"></div>
  <p class="projects-lead">Lorem ipsum dolor sit amet, consectetur adipisicing elit. Culpa, alias enim placeat earum quos ab.</p>
</section>
<div class="abs grid">
  <div class="tile t1" role="img" aria-label="Photo of a modern office building facade">
    <div class="tile-overlay"><b>View more</b>Lorem ipsum dolor sit amet,<br>consectetur adipisicing elit</div>
  </div>
  <div class="tile t2" role="img" aria-label="Photo of a city skyline behind a park with a fountain"></div>
  <div class="tile t3" role="img" aria-label="Photo of a modern villa at dusk with a driveway"></div>
  <div class="tile t4" role="img" aria-label="Photo of a high-rise tower beside palm trees and a pool"></div>
  <div class="tile t5" role="img" aria-label="Rendering of a stone terraced house with green roofs"></div>
  <div class="tile t6" role="img" aria-label="Photo of a row of residential towers beyond green fields"></div>
  <div class="tile t7" role="img" aria-label="Photo of a suburban family house with a garage"></div>
  <div class="tile t8" role="img" aria-label="Rendering of a blue wooden house on house plans"></div>
</div>

<section>
  <h2 class="section-title partners-title" style="font-size:25px">Wolkenfeld Is A Joint Venture Between</h2>
  <div class="divider" style="top:1732px"></div>
  <div class="partner" style="left:99px"><i style="background:#d9272e"></i>Norden Property</div>
  <div class="partner" style="left:356px">Halden Group</div>
  <div class="partner" style="left:613px;color:#1b6a8a"><i style="background:#1b6a8a"></i>Talvik Real Estate</div>
  <div class="partner" style="left:870px;color:#1f5aa6">Brightledger</div>
</section>

<footer>
  <div class="abs footer">
    <div class="fcol" style="left:100px;width:135px">
      <h4>Quick Links</h4>
      <ul class="links"><li>Home</li><li>About Us</li><li>Projects</li><li>Investment</li><li>Legal Notice</li><li>Contact Us</li></ul>
    </div>
    <div class="fcol contact" style="left:311px;width:230px">
      <h4>Contact Information</h4>
      <ul>
        <li><svg width="12" height="14" viewBox="0 0 12 14"><path d="M6 0 A5 5 0 0 1 11 5 C11 9 6 14 6 14 C6 14 1 9 1 5 A5 5 0 0 1 6 0Z" fill="#ddd"/><circle cx="6" cy="5" r="2" fill="#333"/></svg><span>Birkenweg 7/TOP 4B 1220 Vienna<br>- Austria</span></li>
        <li><svg width="12" height="12" viewBox="0 0 12 12"><path d="M2 0 L5 3 L3.5 5 C4.5 7 5 7.5 7 8.5 L9 7 L12 10 L10 12 C5 12 0 7 0 2Z" fill="#ddd"/></svg><span>Phone: +43 1000 2040</span></li>
        <li><svg width="13" height="12" viewBox="0 0 13 12"><rect x="3" y="0" width="7" height="4" fill="#ddd"/><rect x="0" y="4" width="13" height="5" fill="#ddd"/><rect x="3" y="8" width="7" height="4" fill="#ddd" stroke="#333"/></svg><span>Fax: +43 1 000 2041</span></li>
        <li><svg width="13" height="10" viewBox="0 0 13 10"><rect x="0.5" y="0.5" width="12" height="9" fill="none" stroke="#ddd"/><path d="M0.5 0.5 L6.5 5.5 L12.5 0.5" fill="none" stroke="#ddd"/></svg><span>info@wolkenfeld.at</span></li>
      </ul>
    </div>
    <div class="fcol news" style="left:615px;width:205px">
      <h4>Newsletter Sign Up</h4>
      <p>Lorem ipsudolor sit coec adipiscin elitsite amet</p>
      <div class="field">Email Address</div>
      <span class="btn">SUBSCRIBE</span>
    </div>
  </div>
  <div class="abs fbrand"><i></i><span>WOLKENFELD</span></div>
  <div class="abs fsocial">
    <span style="background:#3b5998"></span><span style="background:#29a9e1"></span><span style="background:#0e76a8"></span><span style="background:#f7931e"></span>
  </div>
  <div class="abs copyright">Copyright © 2015 Wolkenfeld.at | All Right Reserved</div>
</footer>

</body>
</html>
```